Verdant Pathworks Business Card

want the back of card to be blue- with the logo in the center
front of card- info plus logo (info being mailing address, email address, and website address )
4 different names with titles to have on cards
1) Dominic Ashvale - Owner
2) Bethany Korvuth- Customer Relationship Specialist
3) Luca Brennwick- Vice President of Sales
4) Neil Umbright- Chief Technology Officer

Target Market(s)

tech company in the government/probation office industry

Industry/Entity Type

Government Office

Contact Information for Business Card

1) Dominic Ashvale - Owner

Colors
0355a3
ffffff

Requirements
Must have
• back side should be blue, with the logo placed in the center
• front side needs to include both the logo, as well as company info (info should include website address, email address, and mailing address)

```html
<!DOCTYPE html>
<html lang="en">
<head>
<meta charset="utf-8">
<title>Verdant Pathworks Business Card</title>
<link href="https://fonts.googleapis.com/css2?family=Noto+Serif:wght@400;600&family=Roboto:wght@400&display=swap" rel="stylesheet">
<style>
  :root {
    --navy: #263a66;
    --steel: #8a8d97;
    --paper: #fbfbfb;
    --backdrop: #b4b2b3;
    --white: #ffffff;
  }
  html, body {
    margin: 0;
    width: 1200px;
    height: 1200px;
    overflow: hidden;
    background: var(--backdrop);
  }
  .canvas { position: relative; width: 1200px; height: 1200px; }

  .card {
    position: absolute;
    border-radius: 22px;
    overflow: hidden;
    background: var(--paper);
  }

  /* Card face with logo */
  .card--logo { left: 238px; top: 118px; width: 712px; height: 419px; }
  .brand {
    position: absolute;
    left: 0; right: 0; top: 200px;
    display: flex; align-items: center; justify-content: center; gap: 16px;
  }
  .brand__mark { width: 26px; height: 26px; background: var(--navy); flex: none; }
  .brand__name {
    font-family: "Noto Serif", serif;
    font-weight: 600;
    font-size: 52px;
    color: var(--navy);
    letter-spacing: 1px;
    white-space: nowrap;
  }
  .site-line {
    position: absolute; left: 0; right: 0; top: 376px;
    display: flex; align-items: center; justify-content: center; gap: 22px;
    font-family: "Roboto", sans-serif; font-size: 18px; color: var(--navy);
  }
  .site-line__rule { width: 48px; height: 3px; background: var(--navy); border-radius: 2px; }
  .band { position: absolute; bottom: 0; height: 15px; }
  .band--navy { left: 0; width: 357px; background: var(--navy); }
  .band--steel { left: 357px; right: 0; background: var(--steel); }

  /* Card face with contact details */
  .card--contact { left: 231px; top: 645px; width: 711px; height: 415px; }
  .card__curve { position: absolute; inset: 0; }
  .person { position: absolute; left: 31px; top: 26px; color: var(--white); }
  .person__name {
    font-family: "Noto Serif", serif; font-weight: 400; font-size: 26px; letter-spacing: 0.5px;
    text-transform: uppercase; margin: 0;
  }
  .person__title { font-family: "Roboto", sans-serif; font-size: 17px; margin: 4px 0 0; }
  .contact {
    position: absolute; left: 31px; top: 244px;
    font-family: "Roboto", sans-serif; font-size: 18px; color: var(--white);
  }
  .contact__address { margin: 0 0 12px; line-height: 30px; }
  .contact__row { display: flex; align-items: center; gap: 14px; height: 26px; }
  .contact__icon { width: 16px; height: 16px; flex: none; }
  .brand--vertical {
    left: 598px; right: auto; top: 207px;
    width: max-content;
    transform: translate(-50%, -50%) rotate(-90deg);
    gap: 12px;
  }
  .brand--vertical .brand__name { font-size: 31px; letter-spacing: 0.5px; }
  .brand--vertical .brand__mark { width: 18px; height: 18px; }
</style>
</head>
<body>
<main class="canvas">

  <section class="card card--logo">
    <div class="brand">
      <span class="brand__mark"></span>
      <span class="brand__name">Verdant Pathworks</span>
    </div>
    <div class="site-line">
      <span class="site-line__rule"></span>
      <span>www.BrinmoreCapital.com</span>
      <span class="site-line__rule"></span>
    </div>
    <div class="band band--navy"></div>
    <div class="band band--steel"></div>
  </section>

  <section class="card card--contact">
    <svg class="card__curve" width="711" height="415" viewBox="0 0 711 415">
      <path d="M0 0 H462 Q398 200 466 415 H0 Z" fill="var(--steel)"/>
      <path d="M0 0 H456 Q390 200 451 415 H0 Z" fill="var(--navy)"/>
    </svg>

    <div class="person">
      <h1 class="person__name">Bethany Korvuth</h1>
      <p class="person__title">Customer Relationship Specialist</p>
    </div>

    <div class="contact">
      <p class="contact__address">418 Larchmont Ave., Fenwick,<br>Easton Vale, US 204781</p>
      <div class="contact__row">
        <svg class="contact__icon" viewBox="0 0 16 16"><path d="M1 5 Q8 0 15 5 L13 7 L11 5 H5 L3 7 Z M3 8 H13 L14 14 H2 Z" fill="var(--white)"/></svg>
        <span>555-014-2270</span>
      </div>
      <div class="contact__row">
        <svg class="contact__icon" viewBox="0 0 16 16"><rect x="1" y="3" width="14" height="10" fill="var(--white)"/><path d="M1 3 L8 9 L15 3" stroke="var(--navy)" stroke-width="1.3" fill="none"/></svg>
        <span>bethany.k@verdantpathworks.com</span>
      </div>
      <div class="contact__row">
        <svg class="contact__icon" viewBox="0 0 16 16"><circle cx="8" cy="8" r="6.5" fill="none" stroke="var(--white)" stroke-width="1.4"/><ellipse cx="8" cy="8" rx="3" ry="6.5" fill="none" stroke="var(--white)" stroke-width="1.2"/><path d="M1.5 8 H14.5" stroke="var(--white)" stroke-width="1.2"/></svg>
        <span>www.verdantpathworks.com</span>
      </div>
    </div>

    <div class="brand brand--vertical">
      <span class="brand__mark"></span>
      <span class="brand__name">Verdant Pathworks</span>
    </div>
  </section>

</main>
</body>
</html>
```